Copperleaf Motorized Shade Business Card

Hello, we've had our logo made. Now we are looking for a clean and cool looking business card. One side can just be the logo with any design elements that might look good with it. The other side will be Name, Phone Number and Email. There will not be an address on the card.

```html
<!DOCTYPE html>
<html lang="en">
<head>
<meta charset="utf-8">
<title>Copperleaf Motorized Shades – Business Card</title>
<link href="https://fonts.googleapis.com/css2?family=Oswald:wght@500;600&family=Montserrat:wght@400;500&display=swap" rel="stylesheet">
<style>
  :root {
    --backdrop: #1c1d20;
    --brand-blue: #0e4689;
    --brand-navy: #0b2f63;
    --deep-navy: #08254e;
    --sky: #1aa3e0;
    --paper: #f3f4f5;
    --white: #ffffff;
  }
  * { margin: 0; padding: 0; box-sizing: border-box; }
  html, body { width: 1200px; height: 874px; overflow: hidden; }
  body {
    background: var(--backdrop);
    display: flex;
    flex-direction: column;
    align-items: center;
    justify-content: center;
    gap: 40px;
  }
  .card {
    width: 630px;
    height: 360px;
    position: relative;
    overflow: hidden;
    border-radius: 3px;
    box-shadow: 0 10px 30px rgba(0,0,0,0.45);
  }

  /* Back: logo side */
  .card-back {
    background: var(--brand-blue);
    display: flex;
    align-items: center;
    justify-content: center;
  }
  .wordmark {
    font-family: "Oswald", sans-serif;
    font-weight: 600;
    text-transform: uppercase;
    text-align: center;
    line-height: 1;
  }
  .card-back .wordmark {
    color: var(--deep-navy);
    font-size: 64px;
    letter-spacing: 1px;
  }
  .wordmark .sub {
    display: block;
    font-size: 0.3em;
    letter-spacing: 0.35em;
    margin-top: 10px;
  }

  /* Front: contact side */
  .card-front { background: var(--paper); }
  .front-top {
    height: 218px;
    display: flex;
    flex-direction: column;
    align-items: center;
    justify-content: center;
    gap: 22px;
  }
  .card-front .wordmark {
    color: var(--brand-navy);
    font-size: 58px;
  }
  .person {
    font-family: "Oswald", sans-serif;
    font-weight: 500;
    font-size: 26px;
    color: var(--brand-navy);
    text-transform: uppercase;
  }
  .person .role {
    font-family: "Montserrat", sans-serif;
    font-size: 18px;
    color: var(--sky);
    margin-left: 4px;
  }
  .contact-band {
    position: absolute;
    left: 0; right: 0; bottom: 0;
    height: 142px;
    background: var(--brand-blue);
    padding: 36px 0 0 60px;
    font-family: "Montserrat", sans-serif;
    font-size: 15px;
    color: var(--white);
    line-height: 1.8;
  }
  .contact-band .sep { margin: 0 8px; }
  .corner-mark {
    position: absolute;
    right: 0; bottom: 0;
    width: 118px; height: 118px;
    background: var(--paper);
    display: flex;
    align-items: center;
    justify-content: center;
  }
  .corner-mark .square {
    width: 54px; height: 54px;
    background: var(--brand-navy);
  }
</style>
</head>
<body>
  <section class="card card-back" aria-label="Card back">
    <div class="wordmark">Copperleaf<span class="sub">Motorized Shades</span></div>
  </section>

  <section class="card card-front" aria-label="Card front">
    <div class="front-top">
      <div class="wordmark">Copperleaf<span class="sub">Motorized Shades</span></div>
      <div class="person">Daniel Hart –<span class="role">PRESIDENT</span></div>
    </div>
    <div class="contact-band">
      <div>P : 555-214-7730<span class="sep"></span>F : 555-418-2096<span class="sep"></span>E : 555-367-1842</div>
      <div>info@copperleafms.com<span class="sep">|</span>www.copperleafms.com</div>
    </div>
    <div class="corner-mark"><div class="square"></div></div>
  </section>
</body>
</html>
```